Brivolt: Electrical Contractor flyer design.

We are looking for a sharp and professional flyer to promote the business's cost for specific jobs and to promote the business.
We are a small electrical business looking to break into the market.
Attached logo to be used and following content to be incorporated. Contact details will be given upon final flyer design.

Internal Power Points: $ 120
External Weather Proof Power Points: $150
T.V. Points: $120 (excludes aerial)
T.V. Mounting: $ 200 (Exclude Leads)
Aerials Starting From: $220 Incudes Mast
LED Down lights: $60 per unti
Ceiling Fans: $150 (Fan Excluded)
Oven & Range Hood Change Overs: $250
A.C. Install: $300
S/B Upgrade: From $600
Safety Switch Installation: $280
Phone Points: $120

Services Incude:

New home wiring
Shop & Office Fit Outs
Re - Wires
Extentions
Garden Lighting
Home Thearters
Home Automation
Power Points
Phone, Data
Feature Lighting
Lighting design and Installation
Ceiling Fans
A.C Installation
Oven & Range hood Installation

*All prices are gst inclusive
**Prices subject to change due to site access.

```html
<!DOCTYPE html>
<html lang="en">
<head>
<meta charset="utf-8">
<title>Brivolt Electrical Flyer</title>
<link href="https://fonts.googleapis.com/css2?family=Ubuntu:wght@400;500;700&display=swap" rel="stylesheet">
<style>
  :root{
    --bg:#d9d8d8;
    --charcoal:#4a4a4d;
    --charcoal-dark:#3d3d40;
    --ink:#1f1f21;
    --orange:#f26a22;
    --orange-deep:#d9602a;
    --peach:#f7b385;
    --grey-band:#a9aaad;
    --white:#ffffff;
  }
  *{box-sizing:border-box;margin:0;padding:0}
  html,body{width:1200px;height:1200px;overflow:hidden}
  body{background:var(--bg);font-family:"Ubuntu",sans-serif;position:relative}

  .page{position:absolute;top:204px;width:560px;height:792px;overflow:hidden;background:var(--charcoal);box-shadow:0 6px 18px rgba(0,0,0,.25)}
  .page--front{left:30px}
  .page--back{left:610px}
  .page-shapes{position:absolute;inset:0;width:560px;height:792px}

  /* front */
  .front-title{position:absolute;left:30px;top:26px;font-size:42px;font-weight:400;color:var(--white);letter-spacing:1px}
  .front-title .accent{color:var(--orange)}
  .price-list{position:absolute;top:92px;left:0;width:560px;list-style:none}
  .price-row{display:flex;align-items:center;height:49px}
  .price-row--warm{background:var(--peach)}
  .price-row--cool{background:var(--grey-band)}
  .price-row .tag{height:100%;display:flex;align-items:center;padding-left:22px;font-size:17px;color:var(--white);
    clip-path:polygon(0 0,calc(100% - 34px) 0,100% 50%,calc(100% - 34px) 100%,0 100%)}
  .price-row--warm .tag{background:var(--orange)}
  .price-row--cool .tag{background:var(--ink)}
  .price-row .price{margin-left:18px;font-size:34px;color:var(--ink);font-weight:400}
  .price-row .price small{font-size:18px;margin-left:10px}
  .price-row .price .from{font-size:20px;margin-right:6px}
  .footnotes{position:absolute;left:40px;top:712px;width:190px;font-size:12px;line-height:15px;color:var(--white);list-style:none}
  .footnotes li{display:flex;gap:8px}
  .footnotes .mark-note{flex:0 0 14px}

  /* back */
  .back-title{position:absolute;left:40px;top:22px;font-size:40px;font-weight:400;color:var(--white);letter-spacing:2px}
  .service-list{position:absolute;top:74px;left:0;list-style:none}
  .service-list li{height:40px;margin-bottom:4px;display:flex;align-items:center;padding-left:38px;padding-right:48px;font-size:21px;color:var(--white);width:max-content;
    clip-path:polygon(0 0,calc(100% - 34px) 0,100% 50%,calc(100% - 34px) 100%,0 100%)}
  .service-list li:nth-child(odd){background:var(--orange)}
  .service-list li:nth-child(even){background:var(--ink)}
  .contact{position:absolute;left:26px;top:710px;font-size:12px;line-height:16px;color:var(--white);list-style:none}
  .contact span{color:var(--orange)}

  /* wordmark */
  .brand{position:absolute;display:flex;align-items:center;gap:8px}
  .brand .mark{width:20px;height:20px;background:var(--orange)}
  .brand .name{font-size:38px;font-weight:700;color:var(--charcoal-dark);letter-spacing:1px}
  .brand .legal{position:absolute;right:0;bottom:-12px;font-size:8px;color:var(--charcoal-dark)}
  .page--front .brand{left:360px;top:712px}
  .page--back .brand{left:370px;top:716px}
</style>
</head>
<body>

<section class="page page--front">
  <svg class="page-shapes" viewBox="0 0 560 792" aria-hidden="true">
    <path d="M400 0 C440 10 455 45 460 92 H560 V0 Z" fill="var(--orange-deep)"/>
    <path d="M400 0 C440 10 455 45 460 92" fill="none" stroke="var(--white)" stroke-width="3"/>
    <path d="M290 792 C300 720 330 680 380 660 L560 640 V792 Z" fill="var(--orange-deep)"/>
    <path d="M300 792 C330 715 420 690 560 680 V792 Z" fill="var(--white)"/>
    <path d="M260 680 L230 792" stroke="var(--white)" stroke-width="3"/>
  </svg>

  <h1 class="front-title"><span class="accent">Services</span> &amp; Prices</h1>

  <ul class="price-list">
    <li class="price-row price-row--warm"><span class="tag" style="width:290px">Internal Power Points:</span><span class="price">$120</span></li>
    <li class="price-row price-row--cool"><span class="tag" style="width:410px">External Weather Proof Power Points:</span><span class="price">$150</span></li>
    <li class="price-row price-row--warm"><span class="tag" style="width:190px">T.V. Points:</span><span class="price">$120<small>(excludes aerial)</small></span></li>
    <li class="price-row price-row--cool"><span class="tag" style="width:220px">T.V. Mounting:</span><span class="price">$200<small>(exclude leads)</small></span></li>
    <li class="price-row price-row--warm"><span class="tag" style="width:290px">Aerials Starting From:</span><span class="price">$200<small>(incudes mast)</small></span></li>
    <li class="price-row price-row--cool"><span class="tag" style="width:260px">LED Down lights:</span><span class="price">$60<small>(per unit)</small></span></li>
    <li class="price-row price-row--warm"><span class="tag" style="width:210px">Ceiling Fans:</span><span class="price">$150<small>(fan excluded)</small></span></li>
    <li class="price-row price-row--cool"><span class="tag" style="width:430px">Oven &amp; Range Hood Change Overs:</span><span class="price">$250</span></li>
    <li class="price-row price-row--warm"><span class="tag" style="width:200px">A.C. Install:</span><span class="price">$300</span></li>
    <li class="price-row price-row--cool"><span class="tag" style="width:220px">S/B Upgrade:</span><span class="price"><span class="from">from</span>$600</span></li>
    <li class="price-row price-row--warm"><span class="tag" style="width:340px">Safety Switch Installation:</span><span class="price">$280</span></li>
    <li class="price-row price-row--cool"><span class="tag" style="width:220px">Phone Points:</span><span class="price">$120</span></li>
  </ul>

  <ul class="footnotes">
    <li><span class="mark-note">*</span><span>All prices are gst inclusive</span></li>
    <li><span class="mark-note">**</span><span>Prices subject to change<br>due to site access.</span></li>
  </ul>

  <div class="brand"><span class="mark"></span><span class="name">Brivolt</span><span class="legal">pty ltd</span></div>
</section>

<section class="page page--back">
  <svg class="page-shapes" viewBox="0 0 560 792" aria-hidden="true">
    <rect width="560" height="792" fill="var(--orange-deep)"/>
    <rect y="440" width="560" height="352" fill="var(--orange)" opacity=".55"/>
    <path d="M0 0 H450 C490 30 505 70 490 120 L270 792 H0 Z" fill="var(--charcoal)"/>
    <path d="M0 440 H375 L270 792 H0 Z" fill="var(--white)" opacity=".04"/>
    <path d="M450 0 C490 30 505 70 490 120 L270 792" fill="none" stroke="var(--white)" stroke-width="3"/>
    <path d="M310 792 C340 725 415 700 560 692 V792 Z" fill="var(--white)"/>
    <path d="M310 792 C340 725 415 700 560 692" fill="none" stroke="var(--orange)" stroke-width="4"/>
  </svg>

  <h2 class="back-title">Services Incude:</h2>

  <ul class="service-list">
    <li>New home wiring</li>
    <li>Shop &amp; Office Fit Outs</li>
    <li>Re - Wires</li>
    <li>Extentions</li>
    <li>Garden Lighting</li>
    <li>Home Thearters</li>
    <li>Home Automation</li>
    <li>Power Points</li>
    <li>Phone, Data</li>
    <li>Feature Lighting</li>
    <li>Lighting design and Installation</li>
    <li>Ceiling Fans</li>
    <li>A.C Installation</li>
    <li>Oven &amp; Range hood Installation</li>
  </ul>

  <ul class="contact">
    <li><span>Email:</span> hello@brivolt.com</li>
    <li><span>Mobile:</span> +61 400 555 019</li>
    <li><span>Website:</span> www.brivolt.com</li>
    <li><span>Facebook:</span> facebook.com/brivolt</li>
  </ul>

  <div class="brand"><span class="mark"></span><span class="name">Brivolt</span><span class="legal">pty ltd</span></div>
</section>

</body>
</html>
```